Plumhart honey labels

we are in need of new labels. we are changing to shorter round cream style honey jars. scalable from 25-100mm tall. We are looking for simple yet elegant
we sell premium varietal honeys from around the USA and locally produced small batch honeys. we are in San Francisco and Sonoma county Calif. for 10 yrs. we strive to supply only the highest quality honey at a premium price point
our logo is gold text on black background, can be found at plumhart.net

Reason: would like to see more designs for a paper wrap around label

Reason: get your designs in so we can choose soon

Target Market(s)

we provide Premium honeys that cannot be found easily elsewhere
at Premium prices. Our customers are socially aware but not afraid to pay more for a premium product

Colors

Designer to choose colors to be used in the design.

Requirements
Must have
• we will be using round jars in 3 sizes, 1.5-4 inches tall, 53mm,63mm,89mm diameter
all will have black lids
will need wrap around labels for labeling machine application
will need simple nutrition label info included
Nice to have
• room on side for nutrition label info
plumhart logo included, of course
space on side for short description of honey
Should not have
• honey dripping off honey dipper or spoon
picture of honeycomb
comic bees or flowers

```html
<!DOCTYPE html>
<html lang="en">
<head>
<meta charset="UTF-8">
<title>Plumhart Honey Label</title>
<link rel="stylesheet" href="https://fonts.googleapis.com/css2?family=Fredoka:wght@500;700&family=Arimo:wght@400&display=swap">
<style>
  :root {
    --page-bg: #ffffff;
    --label-black: #000000;
    --gold: #f2c40f;
    --gold-light: #ffe34a;
    --gold-deep: #e08a12;
    --net-yellow: #fff200;
  }
  html, body {
    margin: 0;
    padding: 0;
    width: 1200px;
    height: 900px;
    overflow: hidden;
    background: var(--page-bg);
  }
  .canvas {
    position: relative;
    width: 1200px;
    height: 900px;
  }
  .label {
    position: absolute;
    left: 280px;
    top: 94px;
    width: 640px;
    height: 712px;
    background: var(--label-black);
  }
  .brand {
    position: absolute;
    left: 0;
    width: 586px;
    top: 98px;
    display: flex;
    justify-content: center;
    align-items: center;
    gap: 10px;
  }
  .brand-name {
    font-family: "Fredoka", sans-serif;
    font-weight: 500;
    font-size: 54px;
    line-height: 1;
    color: var(--gold);
  }
  .brand-dot {
    width: 12px;
    height: 12px;
    border-radius: 50%;
    background: var(--gold);
    margin-top: 22px;
  }
  .rule {
    position: absolute;
    width: 5px;
    background: linear-gradient(to bottom, var(--gold-deep), var(--gold-light) 70%, var(--gold));
  }
  .rule-left { left: 33px; top: 200px; height: 455px; }
  .rule-right { left: 564px; top: 200px; height: 475px; }
  .product-name {
    position: absolute;
    left: 0;
    width: 600px;
    top: 290px;
    margin: 0;
    text-align: center;
    font-family: "Fredoka", sans-serif;
    font-weight: 700;
    font-size: 146px;
    line-height: 1;
    letter-spacing: 2px;
    background: linear-gradient(to bottom, var(--gold-light) 0%, var(--gold) 55%, var(--gold-deep) 100%);
    -webkit-background-clip: text;
    background-clip: text;
    color: transparent;
  }
  .net-weight {
    position: absolute;
    left: 158px;
    top: 626px;
    font-family: "Arimo", sans-serif;
    font-size: 29px;
    color: var(--net-yellow);
  }
</style>
</head>
<body>
  <main class="canvas">
    <section class="label">
      <div class="brand">
        <span class="brand-name">plumhart</span>
        <span class="brand-dot"></span>
      </div>
      <span class="rule rule-left"></span>
      <span class="rule rule-right"></span>
      <h1 class="product-name">HONEY</h1>
      <p class="net-weight">Net Wt.</p>
    </section>
  </main>
</body>
</html>
```